Website design for headhunting agency

The design I need (PSD file) is for a company offering specialised services in recruitment of high-end executive and management positions for businesses.
OBJECTIVES OF THE WEBSITE:
1. Let entrepreneurs and business leaders know about their services and easily have them contact Velnarix if they want more information about their services.
2. Display a list of available carreer opportunities (according to their client's need).
WHAT I NEED:
1st, I need the design for the Home Page ONLY. Once approved, I will need the other pages designed as well. (Here is prototype that we've already developed for the Website that will guide you in the design:
http://demo.quorvaweb.example/velnarix/fr/accueil)
ATTACHED FILES
- Logo
- PDF brochure: Use for inspiration. It is encouraged that you use pictures from this brochure. You can always suggest new ones, as long as they are not expensive to buy and have the same look and feel as the brochure.
HOMEPAGE:
1. Main menu : 6 sections
Accueil | Velnarix | Équipe | Approche | Postes disponibles | Publications
2. Main slider: 4 sections
- Chasseurs de têtes (Headhunters)
- Notre approche (Our Approach)
- Postes cadres disponibles (Executive Careers
Opportunities)
- Contactez-nous (Contact Us)
3. Main Call To Action Boxes :
- Liste Des postes disponibles (Liste of Available Careers
Opportunities)
- Formulaire de contact (contact form)
4. Latest blog articles
- Les derniers articles.
OTHER PAGES (to design once Homepage is approved)
- Velnarix (about us)
- Équipe (our team)
- Approche (our approach)
- Postes disponibles (Career opportunities)
- Publications (blog articles)
- Contact (Contact us)
Target Market(s)
ORGANIZATIONS:
Leaders of organizations seeking to recruit highly qualified staff.
HIGHLY QUALIFIED RESOURCES:
Senior individuals seeking a salary between $70,000 and $ $200,000 annually
PROFESSIONAL SECTORS:
manufacturing : Primary and secondary industries
pharmaceutical
Aerospace
Finances
Retail business
Engineering
Chemical and petrochemical
IT, telecommunications and high technology
Professional Organizations and Association
Industry/Entity Type
Business
Look and feel
Each slider illustrates characteristics of the customer's brand and the style your logo design should communicate.

```html
<!DOCTYPE html>
<html lang="fr">
<head>
<meta charset="utf-8">
<title>Velnarix – Recherche de cadres</title>
<link rel="stylesheet" href="https://fonts.googleapis.com/css2?family=Josefin+Sans:wght@600;700&family=Montserrat:ital,wght@0,300;0,400;0,500;0,600;0,700;1,800&family=Open+Sans:wght@400;600&display=swap">
<style>
:root{
  --teal-dark:#0b5762;
  --teal:#0e8793;
  --accent:#eaa31d;
  --text:#333;
  --rule:#d4d4d4;
  --panel:#ececec;
  --white:#fff;
  --grey-btn:#9c9c9c;
  --blue-box:#72a9cf;
  --yellow-box:#e9b12a;
  --footer:#474747;
  --dark-btn:#3a2a12;
}
*{box-sizing:border-box;margin:0;padding:0}
html,body{width:683px;height:1200px;overflow:hidden;background:var(--white)}
body{position:relative;font-family:"Open Sans",sans-serif;color:var(--text)}

/* Header */
.site-header{position:absolute;left:0;top:0;width:683px;height:58px;background:linear-gradient(#fff,#f1f1f1);border-bottom:1px solid #ddd}
.brand{position:absolute;left:80px;top:28px;display:flex;align-items:center;gap:6px}
.brand-mark{width:12px;height:12px;background:var(--teal-dark)}
.brand-name{font-family:"Montserrat",sans-serif;font-weight:500;font-size:18px;letter-spacing:.6px;color:var(--teal-dark);line-height:1}
.brand-tag{position:absolute;left:126px;top:45px;font-family:"Montserrat",sans-serif;font-size:7.5px;color:var(--teal-dark);line-height:1}
.utility-nav{position:absolute;right:80px;top:6px;display:flex;gap:11px;font-family:"Montserrat",sans-serif;font-size:7.5px;color:#888;letter-spacing:.3px}
.main-nav{position:absolute;right:80px;top:38px;display:flex;gap:12px;font-family:"Montserrat",sans-serif;font-size:8.3px;color:#666;letter-spacing:.1px;white-space:nowrap}
.main-nav .active{color:var(--teal-dark);position:relative}
.main-nav .active::after{content:"";position:absolute;left:0;right:0;top:13px;height:2px;background:var(--teal-dark)}

/* Hero */
.hero{position:absolute;left:0;top:58px;width:683px;height:287px;background:linear-gradient(100deg,#0f7883 0%,#128d98 55%,#0c7480 100%)}
.hero-photo{position:absolute;left:0;top:0;width:440px;height:287px;background:linear-gradient(180deg,#9fc4df 0%,#c9d8e2 45%,#6f7f8c 80%,#4d5a62 100%);clip-path:polygon(0 0,100% 0,78% 100%,0 100%)}
.hero-title{position:absolute;left:445px;top:101px;font-family:"Montserrat",sans-serif;font-weight:300;color:var(--white);line-height:1}
.hero-title .big{font-style:italic;font-weight:800;font-size:22px;display:block}
.hero-title .line{font-size:17px;display:block;margin-top:1px}
.hero-title .l2{padding-left:43px}
.hero-title .l3{padding-left:22px}
.hero-title .tri{display:inline-block;width:0;height:0;border-left:6px solid var(--accent);border-top:5px solid transparent;border-bottom:5px solid transparent;margin-left:2px;vertical-align:2px}
.slider-dots{position:absolute;left:324px;top:354px;display:flex;gap:3px}
.slider-dots span{width:6px;height:6px;border-radius:50%;background:#ccc}
.slider-dots .on{background:var(--teal-dark)}

/* CTA panels */
.cta{position:absolute;left:0;top:368px;width:683px;height:279px;background:var(--panel)}
.section-title{font-family:"Josefin Sans",sans-serif;font-weight:700;font-size:14px;color:#2c2c2c;letter-spacing:0;border-left:3px solid var(--accent);padding-left:6px;line-height:16px;white-space:nowrap}
.jobs{position:absolute;left:80px;top:400px;width:251px}
.jobs-head{display:flex;justify-content:space-between;font-family:"Montserrat",sans-serif;font-size:7.3px;font-weight:600;color:#333;margin-top:14px;padding-bottom:6px;border-bottom:1px solid var(--rule)}
.job{display:flex;justify-content:space-between;font-family:"Montserrat",sans-serif;font-size:7.8px;color:#444;height:18.7px;line-height:18.7px;border-bottom:1px solid #e2e2e2}
.jobs-head + .job{margin-top:5px}
.job:last-child{border-bottom:0}
.btn{display:flex;align-items:center;justify-content:center;font-family:"Montserrat",sans-serif;font-weight:700;font-size:8px;color:var(--white);letter-spacing:.3px}
.btn-more{position:absolute;left:81px;top:591px;width:85px;height:28px;background:var(--grey-btn)}
.contact{position:absolute;left:352px;top:400px;width:251px}
.field{position:absolute;left:352px;width:251px;height:22px;background:var(--white);font-family:"Montserrat",sans-serif;font-size:8px;color:#666;padding:6px 5px}
.btn-send{position:absolute;left:352px;top:591px;width:86px;height:28px;background:var(--teal-dark)}

/* Articles */
.articles-band{position:absolute;left:0;top:647px;width:683px;height:41px;background:var(--teal-dark);text-align:center;font-family:"Josefin Sans",sans-serif;font-weight:700;font-size:18px;color:var(--white);line-height:44px;letter-spacing:.3px}
.band-pointer{position:absolute;left:327px;top:687px}
.article{position:absolute;width:250px;height:88px}
.article-photo{position:absolute;left:0;top:0;width:85px;height:86px;border:3px solid #e4e4e4;background:linear-gradient(160deg,#d9d9d9,#8d8f93 70%,#5c5f63)}
.article-body{position:absolute;left:93px;top:-2px;width:160px}
.article-title{font-family:"Montserrat",sans-serif;font-size:7.9px;font-weight:500;color:#222;line-height:11px}
.article-text{font-family:"Montserrat",sans-serif;font-size:6.5px;color:#999;line-height:11.3px;margin-top:2px}
.article-text a{color:var(--teal-dark);text-decoration:none}

/* Follow / newsletter */
.engage{position:absolute;left:0;top:962px;width:683px;height:135px;background:#f0f0f0}
.box{position:absolute;top:985px;width:250px;height:88px;border-radius:4px}
.box-follow{left:81px;background:var(--blue-box);border:1px solid #5f97be}
.follow-icon{position:absolute;left:111px;top:21px;width:27px;height:27px;background:#2f7bb1;border-radius:3px;border:2px solid #d8e8f3}
.box-label{position:absolute;left:0;right:0;text-align:center;font-family:"Montserrat",sans-serif;font-weight:700;font-size:9.5px;color:var(--white)}
.box-news{left:353px;background:var(--yellow-box);border:1px solid #d49a12}
.news-input{position:absolute;left:9px;top:50px;width:156px;height:23px;background:var(--white);font-family:"Montserrat",sans-serif;font-size:7.5px;color:#555;padding:6px 6px}
.btn-sub{position:absolute;left:171px;top:50px;width:68px;height:23px;background:var(--dark-btn);border-radius:2px;color:var(--white)}

/* Footer */
.site-footer{position:absolute;left:0;top:1097px;width:683px;height:103px;background:var(--footer);text-align:center;font-family:"Montserrat",sans-serif;font-size:6.4px;color:#e6e6e6;letter-spacing:.3px;text-transform:uppercase}
.footer-info{position:absolute;left:0;right:0;top:48px;line-height:9px}
.footer-copy{position:absolute;left:0;right:0;top:85px}
</style>
</head>
<body>

<header class="site-header">
  <div class="brand"><span class="brand-mark"></span><span class="brand-name">VELNARIX</span></div>
  <div class="brand-tag">Recherche de cadres</div>
  <nav class="utility-nav"><span>PLAN DU SITE</span><span>CODE D'ÉTIQUE</span><span>CONTACT</span><span>ENGLISH</span></nav>
  <nav class="main-nav"><span class="active">ACCUEIL</span><span>VELNARIX</span><span>ÉQUIPE</span><span>APPROCHE</span><span>POSTES DISPONIBLES</span><span>PUBLICATIONS</span></nav>
</header>

<section class="hero">
  <div class="hero-photo" role="img" aria-label="Executive with briefcase walking through an open door onto a city skyline"></div>
  <h1 class="hero-title">
    <span class="big">Executive</span>
    <span class="line l2">Careers<span class="tri"></span></span>
    <span class="line l3">Opportunities</span>
  </h1>
</section>
<div class="slider-dots"><span></span><span></span><span class="on"></span><span></span></div>

<section class="cta"></section>
<div class="jobs">
  <h2 class="section-title">LISTE DES POSTES DISPONIBLES</h2>
  <div class="jobs-head"><span>VACANCY TITLE</span><span>CLOSING DATE</span></div>
  <div class="job"><span>Customer Service Officer</span><span>31-Dec-2013</span></div>
  <div class="job"><span>Sales Manager, Moulding</span><span>06-Sep-2013</span></div>
  <div class="job"><span>Market Intelligence Specialist</span><span>01-Sep-2013</span></div>
  <div class="job"><span>Marketing Analyst</span><span>31-Dec-2013</span></div>
  <div class="job"><span>Execution Supervisor - Mechanical / Civil</span><span>28-Aug-2013</span></div>
  <div class="job"><span>Contracts Specialist (G&amp;I)</span><span>16-Aug-2013</span></div>
  <div class="job"><span>Senior C&amp;B Specialist</span><span>31-Aug-2013</span></div>
</div>
<div class="btn btn-more">VIEW MORE</div>

<div class="contact"><h2 class="section-title">FORMULAIRE DE CONTACT</h2></div>
<div class="field" style="top:429px">First Name</div>
<div class="field" style="top:457px">Email Address</div>
<div class="field" style="top:485px">Phone Number</div>
<div class="field" style="top:512px;height:70px">Message</div>
<div class="btn btn-send">SEND</div>

<h2 class="articles-band">LES DERNIERS ARTICLES</h2>
<svg class="band-pointer" width="30" height="16" viewBox="0 0 30 16"><polygon points="0,0 30,0 15,15" fill="#0b5762"/></svg>

<article class="article" style="left:81px;top:733px">
  <div class="article-photo" role="img" aria-label="Portrait of a smiling executive in a suit"></div>
  <div class="article-body">
    <h3 class="article-title">Lorem ipsum dolor sit amet, consectetur adipiscing elit.</h3>
    <p class="article-text">Lorem ipsum dolor sit amet, consectetur adipiscing elit, sed do eiusmod tempor incididunt ut labore et dolore magna aliqua. Ut enim ad minim veniam, quis nostrud exercitation ullamco laboris nisi ut aliquip ex ea commodo consequat. <a href="#">Read more...</a></p>
  </div>
</article>
<article class="article" style="left:353px;top:733px">
  <div class="article-photo" role="img" aria-label="Portrait of a businessman in an office"></div>
  <div class="article-body">
    <h3 class="article-title">Lorem ipsum dolor sit amet, consectetur adipiscing elit.</h3>
    <p class="article-text">Lorem ipsum dolor sit amet, consectetur adipiscing elit, sed do eiusmod tempor incididunt ut labore et dolore magna aliqua. Ut enim ad minim veniam, quis nostrud exercitation ullamco laboris nisi ut aliquip ex ea commodo consequat. <a href="#">Read more...</a></p>
  </div>
</article>
<article class="article" style="left:81px;top:845px">
  <div class="article-photo" role="img" aria-label="Portrait of a manager in a suit"></div>
  <div class="article-body">
    <h3 class="article-title">Lorem ipsum dolor sit amet, consectetur adipiscing elit.</h3>
    <p class="article-text">Lorem ipsum dolor sit amet, consectetur adipiscing elit, sed do eiusmod tempor incididunt ut labore et dolore magna aliqua. Ut enim ad minim veniam, quis nostrud exercitation ullamco laboris nisi ut aliquip ex ea commodo consequat. <a href="#">Read more...</a></p>
  </div>
</article>
<article class="article" style="left:353px;top:845px">
  <div class="article-photo" role="img" aria-label="Portrait of a senior professional in a light shirt"></div>
  <div class="article-body">
    <h3 class="article-title">Lorem ipsum dolor sit amet, consectetur adipiscing elit.</h3>
    <p class="article-text">Lorem ipsum dolor sit amet, consectetur adipiscing elit, sed do eiusmod tempor incididunt ut labore et dolore magna aliqua. Ut enim ad minim veniam, quis nostrud exercitation ullamco laboris nisi ut aliquip ex ea commodo consequat. <a href="#">Read more...</a></p>
  </div>
</article>

<section class="engage"></section>
<div class="box box-follow">
  <span class="follow-icon"></span>
  <div class="box-label" style="top:55px">SUIVEZ-NOUS SUR LINKORA</div>
</div>
<div class="box box-news">
  <div class="box-label" style="top:23px">INSCRIVEZ-VOUS À L'INFOLETTRE</div>
  <div class="news-input">Please enter your email address</div>
  <div class="btn btn-sub">SUBSCRIBE</div>
</div>

<footer class="site-footer">
  <p class="footer-info">Velnarix inc. 58, rue des Érables, bureau 310, Brossard (Québec), J4W 2T8 Canada<br>
  Téléphone : - Région de Montréal : 450-555-0142, ailleurs en Amérique : 1-800-555-0187, ailleurs dans le monde : 1-800-555-0163<br>
  Télécopieur : 514-555-0119</p>
  <p class="footer-copy">© - 2013 Velnarix - Tous droits réservés</p>
</footer>

</body>
</html>
```